Veterinary Pylon

My veterinary clinic is not clearly visible from the street and I want to place a Pylon next to my driveway. I want a modern, elegant straight Design, the Photo shows the sheduled place. One can see the clinic on our Homepage: www.lindbrook-pet-klinik.at
The last pictures are examples for pylones I like

Target Market(s)

the passing cars often miss my entry...I want to show where to turn left

Colors
3276b5
33a6d7
00a990

Requirements
Must have
• High value, simple elegance, size: 250cm (high) x 100cm (width)
Nice to have
• Our Logo, arrow(?)

A special Text is not necessary but this will be an option:

Biegen sie hier ab und wir biegen es wieder hin!
Should not have
• Too much Color, the colors I have chosen are the possible colors but it‘s not necessary to use them.

```html
<!DOCTYPE html>
<html lang="de">
<head>
<meta charset="utf-8">
<title>Lindbrook Pet Klinik – Pylon</title>
<link rel="stylesheet" href="https://fonts.googleapis.com/css2?family=Archivo+Black&display=swap">
<style>
  :root {
    --navy: #114a92;
    --sky: #2cb8dc;
    --paper: #ffffff;
    --hill-ice: #eaf8fc;
    --hill-mist: #e6eff7;
  }
  * { margin: 0; padding: 0; box-sizing: border-box; }
  html, body { width: 1200px; height: 3000px; overflow: hidden; background: var(--paper); }
  .pylon { position: relative; width: 1200px; height: 3000px; background: var(--paper); overflow: hidden; }

  .brand-dot {
    position: absolute; left: 480px; top: 250px;
    width: 300px; height: 300px; border-radius: 50%;
    background: var(--navy);
  }
  .brand-name {
    position: absolute; left: 160px; top: 790px; width: 865px;
    font-family: "Archivo Black", "Arial Black", sans-serif;
    font-weight: 400; font-size: 128px; line-height: 1;
    color: var(--navy); text-align: center; text-transform: uppercase;
    letter-spacing: 1px; white-space: nowrap;
  }
  .brand-descriptor {
    position: absolute; left: 160px; top: 990px; width: 865px;
    font-family: "Archivo Black", "Arial Black", sans-serif;
    font-weight: 400; font-size: 66px; line-height: 1;
    color: var(--sky); text-align: center; text-transform: uppercase;
    letter-spacing: 26px; padding-left: 26px; white-space: nowrap;
  }

  .turn-sign { position: absolute; left: 413px; top: 1318px; width: 434px; height: 434px; }
  .hills { position: absolute; left: 0; top: 1916px; width: 1200px; height: 1084px; }
  .pet-illustration {
    position: absolute; left: 117px; top: 2360px; width: 937px; height: 640px;
    background: var(--navy);
    border-radius: 120px 120px 0 0;
  }
</style>
</head>
<body>
<main class="pylon">
  <div class="brand-dot"></div>
  <h1 class="brand-name">Lindbrook</h1>
  <p class="brand-descriptor">Pet Klinik</p>

  <svg class="turn-sign" viewBox="0 0 434 434" role="img" aria-label="Pfeil nach links: hier abbiegen">
    <defs>
      <linearGradient id="sign-fill" x1="0" y1="0" x2="1" y2="0">
        <stop offset="0" stop-color="#114a92"/>
        <stop offset="1" stop-color="#2cb8dc"/>
      </linearGradient>
    </defs>
    <circle cx="217" cy="217" r="217" fill="url(#sign-fill)"/>
    <polyline points="189,118 90,217 189,316" fill="none" stroke="#fff" stroke-width="21"/>
    <line x1="92" y1="217" x2="344" y2="217" stroke="#fff" stroke-width="21"/>
  </svg>

  <svg class="hills" viewBox="0 0 1200 1084" aria-hidden="true">
    <path d="M0 0 C150 0 280 40 370 80 L0 400 Z" fill="var(--hill-ice)"/>
    <path d="M0 315 C250 100 550 0 800 0 C950 0 1100 30 1200 70 L1200 1084 L0 1084 Z" fill="var(--hill-mist)"/>
  </svg>

  <div class="pet-illustration" role="img" aria-label="Illustration: Hund und Katze als dunkelblaue Silhouette"></div>
</main>
</body>
</html>
```